Varnel Group Limited Stationary

We are in need of business card and letterhead designs. We are looking for clean modern designs that complement the style and feel of our logo.

```html
<!DOCTYPE html>
<html lang="en">
<head>
<meta charset="utf-8">
<title>Varnel Group Limited – Business Card</title>
<link rel="stylesheet" href="https://fonts.googleapis.com/css2?family=EB+Garamond:wght@400;500&display=swap">
<style>
  :root {
    --backdrop: #dcd9d4;
    --card: #f3f3f2;
    --card-edge: #e2e2e0;
    --brand-blue: #1f4a8a;
    --ink: #4a4a4a;
    --ink-soft: #6b6b6b;
    --watermark: #e6e6e5;
    --rule: #3d5f96;
  }
  * { box-sizing: border-box; margin: 0; padding: 0; }
  html, body { width: 1200px; height: 900px; overflow: hidden; }
  body {
    background: var(--backdrop);
    font-family: "EB Garamond", Georgia, serif;
    color: var(--ink);
    position: relative;
  }
  .card {
    position: absolute;
    top: 301px;
    width: 520px;
    height: 298px;
    background: var(--card);
    border: 1px solid var(--card-edge);
    box-shadow: 0 6px 18px rgba(0,0,0,0.18);
    overflow: hidden;
  }
  .card--front { left: 50px; }
  .card--back { left: 630px; }

  .watermark {
    position: absolute;
    border-radius: 50%;
    border: 34px solid var(--watermark);
  }
  .card--front .watermark { width: 260px; height: 260px; left: -70px; bottom: -120px; }
  .card--back .watermark { width: 250px; height: 250px; right: -50px; top: -90px; }

  .brand {
    display: flex;
    align-items: center;
    gap: 10px;
    position: relative;
  }
  .brand__dot {
    width: 30px; height: 30px;
    border-radius: 50%;
    background: var(--brand-blue);
    flex: none;
  }
  .brand__name {
    font-weight: 500;
    font-size: 30px;
    letter-spacing: 1.5px;
    text-transform: uppercase;
    color: var(--brand-blue);
    line-height: 1;
  }
  .brand-rule {
    height: 1px;
    background: var(--rule);
    position: relative;
  }

  /* front */
  .card--front .brand { position: absolute; left: 118px; top: 108px; }
  .card--front .brand-rule { position: absolute; left: 160px; top: 152px; width: 240px; }
  .card--front .site {
    position: absolute; left: 0; right: 0; top: 166px;
    text-align: center; font-size: 14px; letter-spacing: 0.5px; color: var(--ink);
  }

  /* back */
  .card--back .brand { position: absolute; left: 36px; top: 64px; }
  .brand--small .brand__name { font-size: 24px; }
  .brand--small .brand__dot { width: 24px; height: 24px; }
  .card--back .brand-rule { position: absolute; left: 70px; top: 100px; width: 190px; }

  .address {
    position: absolute; left: 40px; bottom: 34px;
    font-size: 15px; line-height: 1.3; color: var(--ink);
  }
  .address .site-strong { color: var(--brand-blue); }

  .contact {
    position: absolute; right: 36px; top: 112px; width: 210px;
  }
  .contact__name { font-size: 19px; color: var(--ink); }
  .contact__title {
    font-size: 11px; letter-spacing: 1.5px; text-transform: uppercase;
    color: var(--ink-soft); margin: 0 0 10px 22px;
  }
  .contact__list { list-style: none; font-size: 12.5px; line-height: 1.45; }
  .contact__list li { display: flex; gap: 10px; }
  .contact__key { width: 10px; color: var(--brand-blue); font-weight: 500; }
</style>
</head>
<body>
  <section class="card card--front" aria-label="Business card front">
    <div class="watermark" aria-hidden="true"></div>
    <div class="brand">
      <span class="brand__dot" aria-hidden="true"></span>
      <span class="brand__name">Varnel Group</span>
    </div>
    <div class="brand-rule"></div>
    <p class="site">www.VARNELGROUP.com</p>
  </section>

  <section class="card card--back" aria-label="Business card back">
    <div class="watermark" aria-hidden="true"></div>
    <div class="brand brand--small">
      <span class="brand__dot" aria-hidden="true"></span>
      <span class="brand__name">Varnel Group</span>
    </div>
    <div class="brand-rule"></div>
    <address class="address" style="font-style:normal">
      418 W. Harmon St, #2204<br>
      Chicago, IL 60611<br>
      www.<span class="site-strong">VARNEL</span>GROUP.com
    </address>
    <div class="contact">
      <p class="contact__name">Delia Morrow</p>
      <p class="contact__title">Manager</p>
      <ul class="contact__list">
        <li><span class="contact__key">T</span><span>(555) 01 234 56 78</span></li>
        <li><span class="contact__key">M</span><span>(555) 09 876 54 32</span></li>
        <li><span class="contact__key">E</span><span>morrow@varnelgroup.com</span></li>
      </ul>
    </div>
  </section>
</body>
</html>
```